Direct to Consumer extended service contract business with a new disruptive business model needs a

We need a customized wordpress design for a company called 'Tall Harbor Assurance'.
We provide an innovative and unique service contract protection program direct to consumers. This program provides monthly coverage for all electronics purchased in the last 4 years and all electronics the consumer purchases in the future for a low monthly fee. The overall design should communicate a sense of legitimacy, ethics, and superior customer service and support (in an industry that has a huge PR issue to overcome).
Electronics is the first product group, other product groups with different price points to launch in the future..

Target Market(s)

All purchasers of electronic goods...all demographics

Industry/Entity Type

Electronics

Font styles to use
Sans Serif

Requirements
Must have
• Customer Testimonials
Industry News
Customer ratings
Blog posts
Call to action messaging
Like the functional elements and design of bramblequill.example (need to be better)
Nice to have
• Like to see video testimonials
Social network "whats trending related to electronics or service contract industry"
Easy way to register products for warranty

```html
<!DOCTYPE html>
<html lang="en">
<head>
<meta charset="utf-8">
<title>Tall Harbor Assurance – Electronics</title>
<link rel="stylesheet" href="https://fonts.googleapis.com/css2?family=Cabin:wght@400;500;600;700&family=Open+Sans:wght@400;600;700&display=swap">
<style>
:root{
  --green:#1f9a2e;
  --green-text:#3aa84a;
  --blue:#1a9ad6;
  --navy:#2c4e9b;
  --grey-bg:#e6e6e6;
  --grey-soft:#f2f2f2;
  --text:#333333;
  --white:#ffffff;
  --red:#e32b22;
}
*{box-sizing:border-box;margin:0;padding:0}
html,body{width:1200px;height:2601px;overflow:hidden}
body{background:var(--grey-bg);font-family:"Cabin",sans-serif;color:var(--text);position:relative}
.topbar{height:31px;background:linear-gradient(#2fa83a,#167f22);color:var(--white);font-family:"Open Sans",sans-serif;font-size:13px;font-weight:700;text-align:right;padding:8px 12px 0 0;letter-spacing:.2px}
.header{height:97px;background:var(--white);display:flex;align-items:center;justify-content:space-between;padding:0 40px 0 38px}
.brand-name{font-family:"Cabin",sans-serif;font-weight:600;font-size:26px;color:var(--blue);line-height:1}
.main-nav{display:flex;font-size:24px;font-weight:500;color:#222}
.main-nav a{color:inherit;text-decoration:none;margin-left:30px}
.main-nav a.tight{margin-left:20px}
.main-nav a.spaced{margin-left:48px}
.cat-nav{height:59px;background:var(--navy);display:flex;align-items:center;justify-content:space-between;padding:0 22px;font-weight:600;font-size:20px;color:var(--white)}
.hero{height:501px;background:linear-gradient(#dedede,#f7f7f7 85%,#ffffff);position:relative;border-bottom:1px solid #cfcfcf}
.hero-quote{position:absolute;top:26px;left:0;width:100%;text-align:center;font-size:40px;font-weight:500;line-height:38px;color:var(--blue)}
.hero-devices{position:absolute;left:80px;top:128px;width:396px;height:350px;background:linear-gradient(135deg,#2a2a2a 0%,#3a6fb5 40%,#e8eef6 70%,#f39c26 100%);border-radius:6px}
.quote-box{position:absolute;left:572px;top:129px;width:583px;height:329px;background:var(--white);box-shadow:0 0 4px rgba(0,0,0,.15);padding:14px 31px 0}
.quote-title{font-size:40px;font-weight:500;color:var(--green-text);text-align:center;letter-spacing:.5px}
.select{height:58px;border:1px solid #d6d6d6;margin-top:12px;display:flex;align-items:center;justify-content:space-between;padding:0 16px;font-size:27px;color:#1f5fa6}
.select svg{width:26px;height:16px}
.btn-quote{margin-top:24px;height:59px;background:linear-gradient(#36b345,#1b8f28);color:var(--white);font-size:38px;font-weight:600;text-align:center;line-height:59px;letter-spacing:1px}
.section-title{text-align:center;font-size:35px;font-weight:400;letter-spacing:2px;color:var(--text)}
.ratings{height:312px;background:var(--grey-bg);position:relative;padding-top:50px}
.rating-strip{position:absolute;left:61px;top:113px;width:1078px;height:161px;background:var(--white);display:flex;align-items:center;padding-left:18px}
.rating-item{display:flex;align-items:center;width:359px}
.rating-icon{width:98px;height:98px;border-radius:50%;flex:none;margin-right:14px}
.rating-name{font-size:31px;font-weight:500;color:#222;line-height:1}
.rating-desc{font-family:"Open Sans",sans-serif;font-size:17px;line-height:23px;color:#333;margin-top:4px}
.stars{display:flex;gap:5px;margin-top:3px}
.stars svg{width:27px;height:26px}
.arrow{position:absolute;top:175px;width:20px;height:36px}
.blog{height:396px;background:linear-gradient(var(--white) 85%,#f0f0f0);padding-top:29px;border-bottom:1px solid #d9d9d9}
.blog-grid{display:flex;gap:67px;margin:25px 0 0 69px}
.blog-card{width:311px;height:250px;background:var(--grey-soft);box-shadow:0 0 2px rgba(0,0,0,.1)}
.blog-image{height:174px;background:linear-gradient(135deg,#34b257,#5ec47c)}
.blog-caption{padding:8px 14px;font-size:23px;line-height:29px;color:var(--green-text)}
.panels{position:absolute;top:1474px;left:61px;width:1078px;display:flex;gap:19px}
.panel{background:var(--white);height:465px;box-shadow:0 0 3px rgba(0,0,0,.1)}
.news{width:530px;padding:10px 14px 0}
.panel-title{font-size:40px;font-weight:500;color:var(--green-text);text-align:center;letter-spacing:.5px}
.news-item{height:82px;border:1px solid #ddd;background:var(--grey-soft);display:flex;margin-top:8px;padding:8px}
.news-item:first-of-type{margin-top:20px}
.news-thumb{width:110px;height:64px;background:var(--navy);flex:none}
.news-text{margin-left:16px;font-size:17px;line-height:22px;color:var(--green-text)}
.news-date{font-family:"Open Sans",sans-serif;font-size:13px;color:#444;margin-top:3px}
.testimonials{width:529px;padding:10px 24px 0}
.video-main{margin-top:14px;height:264px;background:linear-gradient(90deg,#0f2a57,#1c4585 60%,#13305f);position:relative}
.play{position:absolute;left:200px;top:98px;width:68px;height:68px}
.video-thumbs{display:flex;gap:3px;margin-top:14px}
.video-thumb{flex:1;height:86px;background:linear-gradient(90deg,#0f2a57,#1c4585)}
.social{position:absolute;top:2020px;left:0;width:100%}
.social-grid{position:absolute;top:78px;left:61px;display:flex;gap:38px}
.social-card{width:333px;height:352px;background:var(--white);box-shadow:0 0 3px rgba(0,0,0,.15)}
.social-head{height:46px;color:var(--white);font-size:23px;font-weight:500;padding:8px 10px}
.head-friend{background:linear-gradient(#4d7ab9,#2b5797)}
.head-chirp{background:linear-gradient(#5fd0f6,#22aee3)}
.head-reel{background:linear-gradient(#f3302a,#c90f0f)}
.social-body{padding:14px 24px;font-family:"Open Sans",sans-serif;font-size:11px;color:#555}
.fb-box{border:1px solid #ddd;padding:14px}
.fb-top{display:flex;align-items:center;gap:10px;font-size:13px;color:#2b5797}
.fb-top .sq{width:48px;height:48px;background:#2b5797;flex:none}
.fb-like{background:#3b5998;color:#fff;padding:0 4px;font-size:11px}
.fb-grid{display:grid;grid-template-columns:repeat(5,1fr);gap:6px;margin-top:12px}
.fb-grid span{height:46px;background:#2b5797}
.tweet{display:flex;gap:8px;padding:6px 0;border-bottom:1px solid #eee;line-height:13px;font-size:10px}
.tweet i{width:30px;height:30px;background:#b8a88f;flex:none}
.tweet b{color:#222}
.reel-top{display:flex;gap:12px;font-size:13px;color:#333}
.reel-top .sq{width:58px;height:50px;background:var(--navy)}
.sub-btn{margin-top:6px;background:var(--red);color:var(--white);font-weight:700;font-size:13px;padding:1px 8px;display:inline-block}
.reel-player{margin-top:18px;height:208px;background:linear-gradient(#2a2a2a,#4a4a4a);position:relative}
.reel-player svg{position:absolute;left:130px;top:60px}
.reel-bar{position:absolute;left:0;bottom:0;width:100%;height:14px;background:#111}
.footer{position:absolute;top:2497px;left:0;width:100%;height:104px;background:var(--navy);color:var(--white);text-align:center;font-family:"Open Sans",sans-serif;font-size:14px;font-weight:600;padding-top:30px;line-height:26px}
</style>
</head>
<body>
<div class="topbar">LOGIN - REGISTER - SUPPORT / CALL: 001-ABC-DEF</div>

<header class="header">
  <div class="brand-name">Tall Harbor Assurance</div>
  <nav class="main-nav">
    <a href="#">HOME</a><a href="#">ABOUT</a><a href="#" class="tight">BLOG</a><a href="#" class="spaced">NEWS</a><a href="#" class="spaced">CLIENTS</a>
  </nav>
</header>

<nav class="cat-nav">
  <span>PHONES</span><span>SLATES</span><span>LAPTOPS</span><span>TABLETS</span><span>EREADERS</span><span>SMARTPHONES</span><span>CAMERAS</span><span>TELEVISIONS</span><span>ALL PRODUCTS</span>
</nav>

<section class="hero">
  <p class="hero-quote">“PAY LESS AND CLAIM MORE ON YOUR<br>ELECTRONIC DEVICE INSURANCE”</p>
  <div class="hero-devices" role="img" aria-label="Desktop monitor, tablet and phone showing a website"></div>
  <form class="quote-box">
    <div class="quote-title">GET A QUOTE TODAY</div>
    <div class="select">Select your mobile phone<svg viewBox="0 0 26 16"><path d="M0 0h26L13 16z" fill="#1f5fa6"/></svg></div>
    <div class="select">Select service provider<svg viewBox="0 0 26 16"><path d="M0 0h26L13 16z" fill="#1f5fa6"/></svg></div>
    <div class="btn-quote">GET QUOTE</div>
  </form>
</section>

<section class="ratings">
  <h2 class="section-title">CUSTOMER RAITING</h2>
  <svg class="arrow" style="left:34px" viewBox="0 0 20 36"><path d="M20 0v36L0 18z" fill="#222"/></svg>
  <div class="rating-strip">
    <div class="rating-item">
      <div class="rating-icon" style="background:#333"></div>
      <div><div class="rating-name">Orchard Store</div><div class="rating-desc">some info came here<br>with description.</div>
      <div class="stars"><svg viewBox="0 0 24 23"><path d="M12 0l3.5 7.6 8.5.9-6.3 5.7 1.8 8.3L12 18.3 4.5 22.5l1.8-8.3L0 8.5l8.5-.9z" fill="#e32b22"/></svg><svg viewBox="0 0 24 23"><path d="M12 0l3.5 7.6 8.5.9-6.3 5.7 1.8 8.3L12 18.3 4.5 22.5l1.8-8.3L0 8.5l8.5-.9z" fill="#e32b22"/></svg><svg viewBox="0 0 24 23"><path d="M12 0l3.5 7.6 8.5.9-6.3 5.7 1.8 8.3L12 18.3 4.5 22.5l1.8-8.3L0 8.5l8.5-.9z" fill="#e32b22"/></svg><svg viewBox="0 0 24 23"><path d="M12 0l3.5 7.6 8.5.9-6.3 5.7 1.8 8.3L12 18.3 4.5 22.5l1.8-8.3L0 8.5l8.5-.9z" fill="#e32b22"/></svg><svg viewBox="0 0 24 23"><path d="M12 0l3.5 7.6 8.5.9-6.3 5.7 1.8 8.3L12 18.3 4.5 22.5l1.8-8.3L0 8.5l8.5-.9z" fill="#e32b22"/></svg></div></div>
    </div>
    <div class="rating-item">
      <div class="rating-icon" style="background:#2a2a2a"></div>
      <div><div class="rating-name">Riverbend Store</div><div class="rating-desc">some info came here<br>with description.</div>
      <div class="stars"><svg viewBox="0 0 24 23"><path d="M12 0l3.5 7.6 8.5.9-6.3 5.7 1.8 8.3L12 18.3 4.5 22.5l1.8-8.3L0 8.5l8.5-.9z" fill="#2e7fd6"/></svg><svg viewBox="0 0 24 23"><path d="M12 0l3.5 7.6 8.5.9-6.3 5.7 1.8 8.3L12 18.3 4.5 22.5l1.8-8.3L0 8.5l8.5-.9z" fill="#2e7fd6"/></svg><svg viewBox="0 0 24 23"><path d="M12 0l3.5 7.6 8.5.9-6.3 5.7 1.8 8.3L12 18.3 4.5 22.5l1.8-8.3L0 8.5l8.5-.9z" fill="#2e7fd6"/></svg><svg viewBox="0 0 24 23"><path d="M12 0l3.5 7.6 8.5.9-6.3 5.7 1.8 8.3L12 18.3 4.5 22.5l1.8-8.3L0 8.5l8.5-.9z" fill="#2e7fd6"/></svg><svg viewBox="0 0 24 23"><path d="M12 0l3.5 7.6 8.5.9-6.3 5.7 1.8 8.3L12 18.3 4.5 22.5l1.8-8.3L0 8.5l8.5-.9z" fill="#2e7fd6"/></svg></div></div>
    </div>
    <div class="rating-item">
      <div class="rating-icon" style="background:#e2402c"></div>
      <div><div class="rating-name">Searchly Store</div><div class="rating-desc">some info came here<br>with description.</div>
      <div class="stars"><svg viewBox="0 0 24 23"><path d="M12 0l3.5 7.6 8.5.9-6.3 5.7 1.8 8.3L12 18.3 4.5 22.5l1.8-8.3L0 8.5l8.5-.9z" fill="#6cbf2e"/></svg><svg viewBox="0 0 24 23"><path d="M12 0l3.5 7.6 8.5.9-6.3 5.7 1.8 8.3L12 18.3 4.5 22.5l1.8-8.3L0 8.5l8.5-.9z" fill="#6cbf2e"/></svg><svg viewBox="0 0 24 23"><path d="M12 0l3.5 7.6 8.5.9-6.3 5.7 1.8 8.3L12 18.3 4.5 22.5l1.8-8.3L0 8.5l8.5-.9z" fill="#6cbf2e"/></svg><svg viewBox="0 0 24 23"><path d="M12 0l3.5 7.6 8.5.9-6.3 5.7 1.8 8.3L12 18.3 4.5 22.5l1.8-8.3L0 8.5l8.5-.9z" fill="#6cbf2e"/></svg><svg viewBox="0 0 24 23"><path d="M12 0l3.5 7.6 8.5.9-6.3 5.7 1.8 8.3L12 18.3 4.5 22.5l1.8-8.3L0 8.5l8.5-.9z" fill="#6cbf2e"/></svg></div></div>
    </div>
  </div>
  <svg class="arrow" style="left:1148px" viewBox="0 0 20 36"><path d="M0 0v36L20 18z" fill="#222"/></svg>
</section>

<section class="blog">
  <h2 class="section-title">LATEST BLOG POSTS</h2>
  <div class="blog-grid">
    <article class="blog-card"><div class="blog-image" role="img" aria-label="Blog post image"></div><p class="blog-caption">Lorem ipsum nipsum saye losamu</p></article>
    <article class="blog-card"><div class="blog-image" role="img" aria-label="Blog post image"></div><p class="blog-caption">Lorem ipsum nipsum saye losamu</p></article>
    <article class="blog-card"><div class="blog-image" role="img" aria-label="Blog post image"></div><p class="blog-caption">Lorem ipsum nipsum saye losamu</p></article>
  </div>
</section>

<div class="panels">
  <section class="panel news">
    <h2 class="panel-title">INDUSTRIAL NEWS</h2>
    <div class="news-item"><div class="news-thumb"></div><div class="news-text">Lorem ipsum nipsum saye losamu this kird yua. Heading of news.<div class="news-date">Date: 10-20-2015</div></div></div>
    <div class="news-item"><div class="news-thumb"></div><div class="news-text">Lorem ipsum nipsum saye losamu this kird yua. Heading of news.<div class="news-date">Date: 10-20-2015</div></div></div>
    <div class="news-item"><div class="news-thumb"></div><div class="news-text">Lorem ipsum nipsum saye losamu this kird yua. Heading of news.<div class="news-date">Date: 10-20-2015</div></div></div>
    <div class="news-item"><div class="news-thumb"></div><div class="news-text">Lorem ipsum nipsum saye losamu this kird yua. Heading of news.<div class="news-date">Date: 10-20-2015</div></div></div>
  </section>
  <section class="panel testimonials">
    <h2 class="panel-title">TESTIMONIALS</h2>
    <div class="video-main" role="img" aria-label="Video testimonial from a customer">
      <svg class="play" viewBox="0 0 68 68"><circle cx="34" cy="34" r="34" fill="#6cbf2e"/><path d="M26 18l24 16-24 16z" fill="#fff"/></svg>
    </div>
    <div class="video-thumbs">
      <div class="video-thumb" role="img" aria-label="Video testimonial thumbnail"></div>
      <div class="video-thumb" role="img" aria-label="Video testimonial thumbnail"></div>
      <div class="video-thumb" role="img" aria-label="Video testimonial thumbnail"></div>
    </div>
  </section>
</div>

<section class="social">
  <h2 class="section-title">LATEST FROM SOCIAL MEDIA</h2>
  <div class="social-grid">
    <div class="social-card">
      <div class="social-head head-friend">Like us on Friendwall</div>
      <div class="social-body"><div class="fb-box">
        <div class="fb-top"><span class="sq"></span><div>Tall Harbor Assurance<br><span class="fb-like">Like</span></div></div>
        <p style="margin-top:12px;border-top:1px solid #ddd;padding-top:8px">3,249,061 people like <span style="color:#2b5797">Friendwall Builders</span>.</p>
        <div class="fb-grid"><span></span><span></span><span></span><span></span><span></span><span></span><span></span><span></span><span></span><span></span></div>
        <p style="margin-top:12px;border-top:1px solid #ddd;padding-top:6px">Friendwall social plugin</p>
      </div></div>
    </div>
    <div class="social-card">
      <div class="social-head head-chirp">Latest from Chirpline</div>
      <div class="social-body" style="padding:10px 14px">
        <div class="tweet"><i></i><div><b>techdaily</b> New gadgets arrive this week for every home<br>10 hours ago</div></div>
        <div class="tweet"><i></i><div><b>gearwatch</b> Protect your screen before the next trip out<br>10 hours ago</div></div>
        <div class="tweet"><i></i><div><b>techdaily</b> I meant to save it - now my phone is fixed<br>10 hours ago</div></div>
        <div class="tweet"><i></i><div><b>devicenews</b> Looks like the new tablet lasts longer than the last one they keep saying<br>10 hours ago</div></div>
        <div class="tweet"><i></i><div><b>techdaily</b> My laptop fell on the floor and the claim was done the same day<br>10 hours ago</div></div>
      </div>
    </div>
    <div class="social-card">
      <div class="social-head head-reel">Join us on Reelhub</div>
      <div class="social-body">
        <div class="reel-top"><span class="sq"></span><div>Tall Harbor Assurance<br><span class="sub-btn">Subscribe</span></div></div>
        <div class="reel-player"><svg width="52" height="64" viewBox="0 0 52 64"><path d="M0 0l52 32L0 64z" fill="#2a7fd4"/></svg><div class="reel-bar"></div></div>
      </div>
    </div>
  </div>
</section>

<footer class="footer">
  Home | About Us | Plans | Services | Benefits | Support | Contact Us<br>
  Copyright © 2014 Tall Harbor Assurance
</footer>
</body>
</html>
```